Updated Buisness card/Design

Target Market(s)

Residential clients

Industry/Entity Type

Interior remodeling

Contact Information for Business Card

see mark up

Requirements
Must have
• Logo

```html
<!DOCTYPE html>
<html lang="en">
<head>
<meta charset="utf-8">
<title>Ridgeway Home Builders – Business Card</title>
<link href="https://fonts.googleapis.com/css2?family=Arimo:wght@400;700&display=swap" rel="stylesheet">
<style>
  :root {
    --backdrop: #141415;
    --card: #2a2a2c;
    --accent: #0aa0ee;
    --accent-deep: #0788cf;
    --ink: #f2f2f2;
  }
  * { margin: 0; padding: 0; box-sizing: border-box; }
  html, body {
    width: 1200px; height: 963px; overflow: hidden;
    background: var(--backdrop);
    font-family: "Arimo", Arial, sans-serif;
  }
  .canvas {
    width: 1200px; height: 963px;
    display: flex; align-items: center; justify-content: center;
  }
  .card {
    position: relative;
    width: 980px; height: 560px;
    background: var(--card);
    border-radius: 34px;
    border-bottom: 5px solid var(--accent);
    border-right: 5px solid var(--accent);
    overflow: hidden;
    color: var(--ink);
  }
  .brand {
    position: absolute; left: 70px; top: 66px;
    display: flex; align-items: center; gap: 14px;
  }
  .brand-mark {
    width: 24px; height: 24px; background: var(--accent);
  }
  .brand-name {
    font-size: 30px; font-weight: 700; letter-spacing: 1px;
    text-transform: uppercase; color: var(--ink);
  }
  .address {
    position: absolute; left: 70px; top: 136px;
    font-size: 22px; line-height: 1.4;
  }
  .contacts {
    position: absolute; left: 70px; top: 232px;
    list-style: none; font-size: 22px; line-height: 1.5;
  }
  .contacts li { display: flex; align-items: center; gap: 12px; }
  .contacts svg { width: 18px; height: 18px; flex: none; }
  .holder {
    position: absolute; right: 70px; top: 170px; text-align: right;
  }
  .holder-name {
    font-size: 34px; font-weight: 700; color: var(--accent);
    text-transform: uppercase; letter-spacing: 1px;
  }
  .holder-license { font-size: 22px; margin-top: 10px; }
  .brand-decoration {
    position: absolute; left: 470px; top: 330px; right: 0; bottom: 0;
    background: linear-gradient(135deg, var(--accent) 0%, var(--accent-deep) 100%);
    border-top-left-radius: 18px;
  }
</style>
</head>
<body>
<main class="canvas">
  <article class="card">
    <div class="brand">
      <span class="brand-mark"></span>
      <span class="brand-name">Ridgeway Home Builders</span>
    </div>

    <p class="address">482 Cedar Ridge Rd, Suite 210<br>Fairview, CA 90000</p>

    <ul class="contacts">
      <li>
        <svg viewBox="0 0 24 24" fill="none" stroke="var(--accent)" stroke-width="2"><path d="M5 3h4l2 5-3 2a12 12 0 0 0 6 6l2-3 5 2v4a2 2 0 0 1-2 2A17 17 0 0 1 3 5a2 2 0 0 1 2-2z"/></svg>
        555.010.2471
      </li>
      <li>
        <svg viewBox="0 0 24 24" fill="none" stroke="var(--accent)" stroke-width="2"><rect x="6" y="2" width="12" height="20" rx="2"/><line x1="11" y1="18" x2="13" y2="18"/></svg>
        555.014.3308
      </li>
      <li>
        <svg viewBox="0 0 24 24" fill="none" stroke="var(--accent)" stroke-width="2"><rect x="2" y="5" width="20" height="14" rx="1"/><path d="M2 6l10 7 10-7"/></svg>
        daniel@ridgewayhome.com
      </li>
      <li>
        <svg viewBox="0 0 24 24" fill="none" stroke="var(--accent)" stroke-width="2"><circle cx="12" cy="12" r="10"/><path d="M2 12h20M12 2a15 15 0 0 1 0 20M12 2a15 15 0 0 0 0 20"/></svg>
        www.ridgewayhome.com
      </li>
    </ul>

    <div class="holder">
      <p class="holder-name">Daniel Reyes</p>
      <p class="holder-license">CA Contractors License - 123456</p>
    </div>

    <div class="brand-decoration" role="img" aria-label="Large company brand mark as corner decoration"></div>
  </article>
</main>
</body>
</html>
```